Yoga/movement guide/teacher for adult yoga practice and kid yoga

What is the positioning or mission statement of your company? to guide individuals in a yoga-based safe and sustainable movement practice applicable to all ages and body types. Currently my focus is working with children in daycare and school settings, but my goal is to expand into private yoga practice for adults, and potentially as part of rented space in studios. I hope to find a way to work with children AND adults (so would love for logo to be appealing to both), but current focus is with children based on need and demand in the community. yoga for children also compliments my backround as a pediatrician/neonatologist, and I greatly miss interacting with children. I also want to emphasize a yoga/movement practice that is focused more on what one feels internally through movement. NOT what one looks like asthetically. I believe in removing all mirrors from yoga/movement practice. It should be an experience of movement/poses/yoga through appropriate cueing and education. It is not about the details of how far the knee should bend, or how high the leg should be. Focusing on foudation first, core, then core engagement and ultimately expression of poses/movements. A focus on strength, stability and mobility, not just flexibility, which is the common perception/association with yoga. I also want individuals to learn to be an advocate of their own health. Through guidance, I hope for individuals to connect with their body so they know themselves so well to be able to advocate for themselves in the modern healthcare world. This internal experience and connection is so essential in a world where modern medicine has become a business and it is all about making a dollar. the connection with patients is lost, and individuals need to learn to empower themselves and through their new found voice to be able to articulate what is wrong.<br/>Does your company have a tagline or slogan that should be included with the logo? "Practice Glowing Motion"<br/>What do you hope your company can be known for? Accessible yoga for a sustained practice. A guided movement practice where one gains information and knowledge of oneself through a mind/body connection. For one feel good physically with a new awaraness of their internal radiance that exists in all beings. Physical rejuvenation egnites a light and increases energy to flow through the physical body, which ultimately tranlates into works of kindness for others and out in the world. <br/>What color palettes might you prefer? why? love the colors currently chosen<br/>Where will the logo be primarily used? initially business cards, but hopefully future websites, t-shirts, and potentially local magazine adds. Also starting with a small couple of banners for community events in the area. I currently practice as a nomad out of my car :)<br/>Are there any elements you would prefer to see in the logo? Movement. A modern depiction of a human body/figure practicing movement. Hoping to avoid a stereotypical yoga pose per say, just because I want to people to think of it more of a movement practice with yoga roots. Modern yoga. There are elements of breathing and connecting with oneself through the flow of breath and movement, but I do not focus on the meditative/cerebral aspect of the yoga practice. What I teach is almost reaching a meditative state through movement. I personally don't practice, nor resonate with just seated meditation. just not my thing :)<br/>In your opinion, what defines a well-designed logo? curiosity. enough info for individuals to think they know what it means, but want to know more. invokes curiosity, but not too abstract. Reproducible. not too complicated. I want also to invoke a community feel, so a design that appeals to all people within a community. <br/>What is your preference in reference to icons, typography, spokespeople (characters), etc.? modern design. I love the idea of a logo for my purposes, to invoke a sense of movement from within. So not too static. <br/>What words or icons must be included in the logo? movement with yoga roots. <br/>What logos do you like and why? A representation, but not exact. I think some ambiguity is intriguing for others, and also memorable. I want it to be an artistic representation of movement/yoga<br/>What logos do you dislike and why? too busy, too loud. <br/>In your opinion, what is the primary purpose for a logo? association<br/>Who is the primary target audience? (who is most likely to use your services/product?) Children and their parents, but ultimately to expand into teaching adults. I even have aspirations of prenatal and post-natal yoga. Potentially incorporating infants. <br/>Who currently uses your product the most? n/a (working in schools/daycare currently. It is currently all volunteer)<br/>Are you pleased with the range of people your company serves? n/a<br/>Are you looking to expand, modify, or completely change your target audience? or will it remain the same? yes! expand into an adult audience. <br/>How do you plan to focus on your target audience? currently by working through schools and daycares. hopefully ultimately through after school care programs and then offering kid yoga in an existing yoga studio (working on this with Q Loft in Ridgeland, currently)<br/>What are your main forms of advertising? word of mouth, schools, daycares. Happy kids talking to their parents about the yoga class they took and happy teachers :)<br/>How do most customers find out about your company?<br/>Which gender are you targeting? All genders! However, with kid yoga, often the maternal individual in the child's life is more involved with decision making as far as extracurricular activities

Target Market(s)

individuals and families interested in wellness and feeling great

Contact Information for Business Card

Dana Whitmore
Yoga Instructor
RYT-200, RCYT

certified yoga teacher for adults and children

Colors

Designer to choose colors to be used in the design.

Requirements
Must have
• "Practice Glowing Motion"
Nice to have
• logo with same colors

```html
<!DOCTYPE html>
<html lang="en">
<head>
<meta charset="utf-8">
<title>Brightfield Studios – Business Card</title>
<link href="https://fonts.googleapis.com/css2?family=Roboto:ital,wght@0,300;0,400;1,300;1,400&display=swap" rel="stylesheet">
<style>
  :root {
    --backdrop: #2a2a2c;
    --card-white: #ffffff;
    --teal: #6ccbd1;
    --sun-yellow: #f5da3c;
    --stone-grey: #8a8a8a;
    --text-on-teal: #ffffff;
    --wordmark-grey: #7d7d7d;
  }
  html, body {
    margin: 0;
    width: 1200px;
    height: 900px;
    overflow: hidden;
    background: var(--backdrop);
    font-family: "Roboto", sans-serif;
  }
  .business-card {
    position: absolute;
    left: 75px;
    top: 150px;
    width: 1050px;
    height: 600px;
    background: var(--card-white);
    overflow: hidden;
    box-shadow: 0 20px 50px rgba(0,0,0,0.5);
  }
  .card-waves {
    position: absolute;
    inset: 0;
  }
  .wave-teal { fill: var(--teal); }
  .wave-yellow { fill: none; stroke: var(--sun-yellow); stroke-width: 16; }
  .wave-grey { fill: none; stroke: var(--stone-grey); stroke-width: 16; }

  .teacher-name {
    position: absolute;
    left: 330px;
    top: 70px;
    margin: 0;
    font-size: 44px;
    font-weight: 400;
    font-style: italic;
    color: var(--text-on-teal);
  }
  .teacher-role {
    position: absolute;
    left: 330px;
    top: 132px;
    margin: 0;
    width: 300px;
    font-size: 22px;
    font-weight: 300;
    font-style: italic;
    line-height: 1.3;
    color: var(--text-on-teal);
  }
  .contact-list {
    position: absolute;
    left: 80px;
    top: 330px;
    margin: 0;
    padding: 0;
    list-style: none;
    color: var(--text-on-teal);
    font-size: 22px;
    font-weight: 400;
  }
  .contact-item {
    display: flex;
    align-items: flex-start;
    gap: 12px;
    margin-bottom: 10px;
    line-height: 1.3;
  }
  .contact-icon {
    flex: none;
    width: 28px;
    height: 28px;
  }
  .contact-divider {
    flex: none;
    width: 2px;
    align-self: stretch;
    background: var(--text-on-teal);
    transform: skewX(-20deg);
  }

  .brand-lockup {
    position: absolute;
    left: 620px;
    top: 250px;
    width: 400px;
    text-align: center;
  }
  .brand-name {
    display: flex;
    align-items: center;
    justify-content: center;
    gap: 14px;
    margin: 0;
    font-size: 44px;
    font-weight: 300;
    color: var(--wordmark-grey);
    line-height: 1.05;
  }
  .brand-dot {
    width: 26px;
    height: 26px;
    border-radius: 50%;
    background: var(--sun-yellow);
    flex: none;
  }
  .brand-tagline {
    margin: 14px 0 0;
    font-size: 16px;
    font-weight: 400;
    letter-spacing: 3px;
    text-transform: uppercase;
    color: var(--teal);
  }
</style>
</head>
<body>
  <section class="business-card">
    <svg class="card-waves" width="1050" height="600" viewBox="0 0 1050 600" aria-hidden="true">
      <path class="wave-teal" d="M0 0 H760 C660 40 620 120 580 260 C540 400 490 560 380 600 H0 Z"/>
      <path class="wave-yellow" d="M800 -10 C700 40 660 120 620 260 C580 400 530 560 420 610"/>
      <path class="wave-grey" d="M850 -10 C750 40 700 120 660 260 C620 400 570 560 470 610"/>
    </svg>

    <h1 class="teacher-name">Dana Whitmore</h1>
    <p class="teacher-role">Teacher for adult yoga practice and kid yoga</p>

    <ul class="contact-list">
      <li class="contact-item">
        <svg class="contact-icon" viewBox="0 0 28 28" aria-label="Phone">
          <circle cx="14" cy="14" r="13" fill="#fff"/>
          <path d="M10 7 l3 3 -2 2 c1 2 3 4 5 5 l2 -2 3 3 -2 2 c-5 0 -11 -6 -11 -11 z" fill="#6ccbd1"/>
        </svg>
        <span class="contact-divider"></span>
        <span>555-014-2837</span>
      </li>
      <li class="contact-item">
        <svg class="contact-icon" viewBox="0 0 28 28" aria-label="Email">
          <circle cx="14" cy="14" r="13" fill="#fff"/>
          <rect x="7" y="9" width="14" height="10" fill="none" stroke="#6ccbd1" stroke-width="2"/>
          <path d="M7 9 l7 6 7 -6" fill="none" stroke="#6ccbd1" stroke-width="2"/>
        </svg>
        <span class="contact-divider"></span>
        <span>Danawhitmore@example.com</span>
      </li>
      <li class="contact-item">
        <svg class="contact-icon" viewBox="0 0 28 28" aria-label="Address">
          <circle cx="14" cy="14" r="13" fill="#fff"/>
          <path d="M14 22 c-4 -5 -6 -8 -6 -11 a6 6 0 0 1 12 0 c0 3 -2 6 -6 11 z" fill="#6ccbd1"/>
          <circle cx="14" cy="11" r="2.2" fill="#fff"/>
        </svg>
        <span class="contact-divider"></span>
        <span>118 Larkspur Lane NE<br>Suite 210, Ridgewood, MI 49500</span>
      </li>
    </ul>

    <div class="brand-lockup">
      <p class="brand-name"><span class="brand-dot"></span>Brightfield Studios</p>
      <p class="brand-tagline">Practice Glowing Motion</p>
    </div>
  </section>
</body>
</html>
```